Brivoza banner and eDM design

We need banner ads and an eDM header to promote Brivoza.com.au (not currently live but logo and site design complete).

Banners should ideally be in flash with back-up gifs but we would be open to just animated gifs as well.

Banner sizes to be delivered are:
300x250
729x90
468x60
160x600

Best to keep banner file size under 25kb if possible (based on standard publisher specs)

For the eDM header, it should be around:
600 wide x
150-200 high

The advertising role is to promote the websites services which are related to making HR easy for small business owners - specifically relating to recruitment, induction, engagement and employee exit. I'll attach more details on this.

Target Market(s)

Small and medium business owners - slightly male skew

Industry/Entity Type

Small Business

Requirements
Must have
• Must match the look and feel and colour palette of the logo and website design that will be attached to this brief.

Must look professional

Must follow the copy guide for the frames as outlined in the attachment - there are 2 options for frame 3 listed. I'd like to get 2 sets of banners developed to cover both options.

Must have clear call-to-action
Nice to have
• Nice to have sophisticated animation if possible

I've added two potential images that could be used - either could be used to illustrate the 'Save time and improve results' line -
one focused on finding the right person
one is focused on improving results through a team

You could potentially use a screen grab of the site homepage in the design too - but only if eligible since none of the copy on it is finalised.

```html
<!DOCTYPE html>
<html lang="en">
<head>
<meta charset="utf-8">
<title>Brivoza – Save Time banner</title>
<link rel="stylesheet" href="https://fonts.googleapis.com/css2?family=Arimo:wght@400;700&display=swap">
<style>
  :root {
    --band-dark: #16357a;
    --band-mid: #2a56ad;
    --band-light: #4a7ad0;
    --headline: #8d9fc6;
    --subline: #7f93bf;
    --panel: #ffffff;
    --brand-blue: #1f5fb8;
    --cta-top: #ff8a2a;
    --cta-bottom: #e85f05;
    --cta-text: #ffffff;
    --photo-light: #f4f6fa;
    --photo-mid: #c9d0dc;
    --divider: #4e5f80;
  }
  * { margin: 0; padding: 0; box-sizing: border-box; }
  html, body { width: 1200px; height: 148px; overflow: hidden; background: #ffffff; }
  .banner {
    position: relative;
    width: 1200px;
    height: 148px;
    overflow: hidden;
    font-family: "Arimo", Arial, sans-serif;
    background: linear-gradient(180deg, var(--band-light) 0%, var(--band-mid) 45%, var(--band-dark) 100%);
  }
  .banner__photo {
    position: absolute;
    left: 0; top: 0;
    width: 425px; height: 148px;
  }
  .banner__headline {
    position: absolute;
    left: 481px; top: 26px;
    font-size: 40px;
    font-weight: 700;
    color: var(--headline);
    letter-spacing: -0.5px;
  }
  .banner__subline {
    position: absolute;
    left: 478px; top: 85px;
    font-size: 26px;
    font-weight: 400;
    color: var(--subline);
  }
  .brand-panel {
    position: absolute;
    left: 824px; top: 0;
    width: 363px; height: 77px;
    background: var(--panel);
    display: flex;
    align-items: center;
    justify-content: center;
    gap: 10px;
  }
  .brand-panel__dot {
    width: 34px; height: 34px;
    border-radius: 50%;
    background: var(--brand-blue);
  }
  .brand-panel__name {
    font-size: 42px;
    font-weight: 700;
    color: var(--brand-blue);
    letter-spacing: -0.5px;
  }
  .cta {
    position: absolute;
    left: 892px; top: 90px;
    width: 225px; height: 46px;
    display: flex;
    align-items: center;
    justify-content: center;
    background: linear-gradient(180deg, var(--cta-top), var(--cta-bottom));
    border: 1px solid #c85004;
    color: var(--cta-text);
    font-size: 23px;
    font-weight: 700;
    text-decoration: none;
  }
</style>
</head>
<body>
  <div class="banner">
    <svg class="banner__photo" viewBox="0 0 425 148" aria-hidden="false">
      <defs>
        <linearGradient id="photoTone" x1="0" y1="0" x2="1" y2="1">
          <stop offset="0" stop-color="var(--photo-light)"/>
          <stop offset="1" stop-color="var(--photo-mid)"/>
        </linearGradient>
        <linearGradient id="dividerTone" x1="0" y1="0" x2="0" y2="1">
          <stop offset="0" stop-color="#7687a8"/>
          <stop offset="1" stop-color="var(--divider)"/>
        </linearGradient>
      </defs>
      <rect role="img" aria-label="Photo of a smiling businesswoman in front of a group of business colleagues" x="0" y="0" width="398" height="148" fill="url(#photoTone)"/>
      <polygon points="390,0 404,0 425,74 404,148 390,148 411,74" fill="url(#dividerTone)"/>
    </svg>

    <div class="banner__headline">Save Time</div>
    <div class="banner__subline">and improve results</div>

    <div class="brand-panel">
      <span class="brand-panel__dot"></span>
      <span class="brand-panel__name">Brivoza</span>
    </div>

    <a class="cta" href="#">Find out more</a>
  </div>
</body>
</html>
```